Journal Cover Design Project

The Meridian Review of Rising Trade Nations is a professional journal which aims to provide an international platform for publication of original research on the emerging economies.
The journal is published three times a year and available by subscription. Currently, the cover design is the same for each issue. We are looking to redesign the cover (and interior) of our journal and would like a design that would allow us to change the color scheme for each issue or volume while maintaining a consistent design scheme.
Our design preference is simple and modern with good use of color. Many of our past publications have used abstract maps/globes but we are open to new ideas. We would need a creative way to include text on the cover, possibly a way to present the article titles or main topics for each issue. For example, we like the use of color and the general design in this image: http://www.pictavo-share.example/photos/brightmakerstudio/5120448391/lightbox/
Below is a link to our most recent issue of the journal. You can see an example of the article titles, structure, etc. The website also shows the current cover of the journal (but we do not want the new design to be based off of the current one):
http://mrt.quellpress.example/content/4/2.toc

```html
<!DOCTYPE html>
<html lang="en">
<head>
<meta charset="utf-8">
<title>The Meridian Review of Rising Trade Nations – Volume 5 Issue 1</title>
<link rel="stylesheet" href="https://fonts.googleapis.com/css2?family=Arimo:wght@400;700&family=Roboto+Condensed:wght@400;700&display=swap">
<style>
  :root {
    --page: #ffffff;
    --paper: #ffffff;
    --ink: #111111;
    --band: #231f20;
    --magenta: #ec008c;
    --magenta-soft: #f25cb4;
    --panel: rgba(20, 14, 16, 0.86);
    --grey-light: #d9d9d9;
    --grey-mid: #8a8a8a;
  }
  * { box-sizing: border-box; margin: 0; padding: 0; }
  html, body {
    width: 1001px; height: 1200px; overflow: hidden;
    background: var(--page);
  }
  .cover {
    position: absolute; left: 78px; top: 30px;
    width: 846px; height: 1110px;
    background: var(--paper);
    overflow: hidden;
    font-family: "Arimo", Arial, sans-serif;
  }
  .issue-date {
    position: absolute; left: 78px; top: 116px;
    color: var(--magenta);
    font-family: "Roboto Condensed", Arial, sans-serif;
    font-weight: 700; font-size: 22px; letter-spacing: 0.5px;
  }
  .masthead {
    position: absolute; left: 0; top: 264px;
    width: 100%; height: 216px;
    background: var(--band);
    color: #fff;
  }
  .masthead-title {
    position: absolute; left: 62px; top: 22px;
    font-weight: 700; font-size: 86px; line-height: 1; letter-spacing: -1.5px;
  }
  .masthead-subtitle {
    position: absolute; left: 66px; top: 122px;
    font-weight: 700; font-size: 41px; line-height: 1; letter-spacing: -0.5px;
  }
  .field {
    position: absolute; left: 0; top: 480px;
    width: 100%; height: 630px;
    background: linear-gradient(180deg, var(--magenta) 0%, var(--magenta-soft) 50%, var(--magenta) 100%);
  }
  .globe-art {
    position: absolute; left: 300px; top: 0;
    width: 440px; height: 470px;
    border-radius: 50%;
    background: radial-gradient(circle at 45% 40%, var(--grey-light) 0%, #b5b5b5 50%, var(--grey-mid) 100%);
    opacity: 0.85;
  }
  .contents {
    position: absolute; left: 462px; top: 96px;
    width: 384px; list-style: none;
  }
  .article {
    height: 80px; margin-bottom: 20px;
    background: var(--panel);
    color: #fff;
    padding: 10px 14px 0 16px;
    font-family: "Roboto Condensed", Arial, sans-serif;
  }
  .article-title {
    display: block; font-weight: 700; font-size: 25px; line-height: 1.05;
  }
  .article-deck {
    display: block; font-weight: 700; font-size: 13.5px; line-height: 1.2; margin-top: 3px;
  }
  .volume-mark {
    position: absolute; left: 50px; top: 245px;
    color: var(--ink);
    font-family: "Roboto Condensed", Arial, sans-serif; font-weight: 700;
  }
  .volume-label {
    position: absolute; left: 0; top: 96px;
    transform: rotate(-90deg); transform-origin: left top;
    font-size: 22px; letter-spacing: 0.5px;
  }
  .volume-number {
    position: absolute; left: 28px; top: -18px;
    font-size: 132px; line-height: 1;
  }
  .issue-label {
    position: absolute; left: 2px; top: 112px; white-space: nowrap;
    font-size: 24px;
  }
  .publishers {
    position: absolute; left: 50px; top: 566px;
    display: flex; gap: 10px; align-items: center;
  }
  .publisher {
    display: flex; align-items: center; gap: 5px;
    background: #fff; padding: 4px 8px; height: 34px;
    font-family: "Roboto Condensed", Arial, sans-serif;
    font-weight: 700; font-size: 12px; color: var(--band);
  }
  .publisher-dot {
    width: 12px; height: 12px; border-radius: 50%; background: var(--magenta);
  }
</style>
</head>
<body>
  <main class="cover">
    <p class="issue-date">AUGUST 2012</p>

    <header class="masthead">
      <h1 class="masthead-title">Meridian Review</h1>
      <p class="masthead-subtitle">of Rising Trade Nations</p>
    </header>

    <section class="field">
      <div class="globe-art" role="img" aria-label="Grey wireframe globe over a magenta grid of curved lines"></div>

      <ul class="contents">
        <li class="article">
          <span class="article-title">Construction and Analysis</span>
          <span class="article-deck">of a Global GDP Growth Model for<br>185 Countries through 2050</span>
        </li>
        <li class="article">
          <span class="article-title">A New Vision for Mexico 2042</span>
          <span class="article-deck">Achieving Prosperity for All</span>
        </li>
        <li class="article">
          <span class="article-title">India 2039</span>
          <span class="article-deck">Transforming Agriculture: Productivity,<br>Markets, and Institutions</span>
        </li>
        <li class="article">
          <span class="article-title">New Directions</span>
          <span class="article-deck">for Water Management in Indian Agriculture</span>
        </li>
      </ul>

      <div class="volume-mark">
        <span class="volume-label">VOLUME</span>
        <span class="volume-number">5</span>
        <span class="issue-label">ISSUE 1</span>
      </div>

      <footer class="publishers">
        <span class="publisher"><span class="publisher-dot"></span>Quell Press</span>
        <span class="publisher"><span class="publisher-dot"></span>Rising Nations Circle</span>
      </footer>
    </section>
  </main>
</body>
</html>
```